Webdesign Bestattung Helga Wendrich
Zielgruppe
es handelt sich um ein Bestattungsunternehmen // Ziel des Unternehmens ist die Ansprache von Hinterbliebenen. Es sollen klare Informationen transportiert werden und schnelle Hilfe im Trauerfall angeboten werden.
Aufgabenstellung
- btte beachten -> der Name lautet jetzt 'Bestattung Helga Wendrich'
-Seite soll einladen und nicht zu 'depressiv' sein
- berücksichtigen Sie bitte die KOntaktmöglichkeiten für die einzelnen Standort -> präsent platzieren
- ganz wenig schwarz & keine schwarzen Balken
- klare Informationen auf der Startseite
- schneller Zugang zu Kontaktmöglichkeiten
- Layout aufgelockert gern etwas geschwungenen Elemente
- Farbgebung Magenta & Gold / punktuell schwarz aber sehr dezent
- modern trotz des schweren Themas

```html
<!DOCTYPE html>
<html lang="en">
<head>
<meta charset="utf-8">
<title>Bestattung Helga Wendrich</title>
<link rel="stylesheet" href="https://fonts.googleapis.com/css2?family=Playfair+Display:ital,wght@1,400;1,500&family=Poppins:wght@400;500&display=swap">
<style>
:root{
  --magenta:#e0067a;
  --gold:#ab9378;
  --text:#6a6a6a;
  --light:#f4f4f4;
  --white:#ffffff;
  --dark:#1c1c1c;
}
*{box-sizing:border-box;margin:0;padding:0}
html,body{width:1200px;height:4392px;overflow:hidden}
body{font-family:"Poppins",sans-serif;color:var(--text);background:var(--white);position:relative}
.serif{font-family:"Playfair Display",serif;font-style:italic;text-transform:uppercase}

/* header */
.site-header{position:absolute;top:0;left:0;width:1200px;height:134px;border-bottom:3px solid var(--magenta);background:var(--white)}
.brand{position:absolute;left:66px;top:56px;font-family:"Playfair Display",serif;font-style:italic;font-size:24px;color:#333;letter-spacing:.5px;white-space:nowrap}
.contact-top{position:absolute;right:68px;top:38px;display:flex;gap:38px;font-size:13px;color:var(--text)}
.contact-top span{display:flex;align-items:center;gap:9px}
.nav{position:absolute;right:68px;top:83px;display:flex;gap:22px;font-size:13.5px;color:var(--text)}
.nav .active{color:var(--magenta)}

/* hero */
.hero{position:absolute;top:137px;left:0;width:1200px;height:620px;background:#ececec}
.hero-photo{position:absolute;inset:0;background:linear-gradient(100deg,#dbe6cf 0%,#eef1ea 28%,#f2f2f2 50%,#e9e9e9 100%)}
.hero-card{position:absolute;left:526px;top:178px;width:514px;height:335px;background:var(--white);overflow:hidden}
.hero-card .band{height:42px;background:var(--magenta);color:var(--white);font-size:26px;line-height:34px;padding:4px 34px}
.hero-card .t1{position:absolute;left:42px;top:64px;font-size:48px;line-height:56px;color:var(--gold);white-space:nowrap}
.hero-card .t2{position:absolute;left:26px;top:120px;font-size:78px;line-height:80px;color:var(--gold);white-space:nowrap}
.call-btn{position:absolute;left:1087px;top:527px}

/* intro */
.intro{position:absolute;top:757px;left:0;width:1200px;height:318px;background:var(--light)}
.intro .kicker{position:absolute;left:66px;top:64px;font-size:13.5px}
.intro h2{position:absolute;left:66px;top:88px;font-size:50px;line-height:47px;color:var(--gold);font-weight:400;white-space:nowrap}
.btn{display:inline-block;background:var(--magenta);color:var(--white);font-size:17px;font-weight:500}
.intro .btn{position:absolute;left:66px;top:205px;padding:10px 17px}
.intro .copy{position:absolute;left:643px;top:66px;width:490px;font-size:13.5px;line-height:24px}
.intro .copy p+p{margin-top:16px}

/* services */
.services-head{position:absolute;top:1148px;left:66px;width:1068px}
.services-head .kicker{font-size:13.5px}
.services-head h2{font-size:102px;line-height:100px;color:var(--gold);font-weight:400;margin-top:4px}
.services-head .btn{position:absolute;right:0;top:64px;width:194px;height:45px;text-align:center;line-height:45px}
.service{position:absolute;left:66px;width:1068px;height:486px}
.service .photo{position:absolute;top:0;width:660px;height:486px}
.service .text{position:absolute;width:240px}
.service h3{font-size:26px;color:var(--gold);font-weight:400;margin-bottom:10px;white-space:nowrap}
.service p{font-size:13.5px;line-height:24px}
.s1{top:1340px}.s1 .photo{left:408px;background:linear-gradient(120deg,#2a2a2e,#4a4a50 55%,#8a8a8c)}
.s1 .text{left:86px;top:146px}
.s2{top:1828px}.s2 .photo{left:0;background:linear-gradient(160deg,#3a3f3a,#5c4032 45%,#55703c)}
.s2 .text{left:730px;top:182px;width:230px}
.s3{top:2316px}.s3 .photo{left:408px;background:linear-gradient(110deg,#1e1e20 30%,#6b6b60 60%,#a7a79a)}
.s3 .text{left:86px;top:160px;width:235px}

/* impressions */
.impressions{position:absolute;top:2934px;left:0;width:1200px;height:999px;background:var(--magenta)}
.impressions h2{position:absolute;left:0;width:1200px;top:100px;text-align:center;font-size:100px;line-height:120px;color:var(--white);font-weight:400}
.grid{position:absolute;left:64px;top:273px;width:1072px;height:594px;display:grid;grid-template-columns:repeat(3,1fr);grid-template-rows:repeat(2,297px)}
.cell{position:relative;display:flex;align-items:center;justify-content:center;text-align:center;color:var(--white);font-size:26px;line-height:34px}
.notch-up::after{content:"";position:absolute;left:50%;bottom:0;margin-left:-30px;border:30px solid transparent;border-top:0;border-bottom-color:var(--magenta);border-bottom-width:28px}
.notch-down::after{content:"";position:absolute;left:50%;bottom:-28px;margin-left:-30px;border:30px solid transparent;border-bottom:0;border-top-color:var(--magenta);border-top-width:28px;z-index:2}
.img-coffin{background:linear-gradient(150deg,#6a4a2a,#d9b89a 45%,#c79e7b)}
.img-urn{background:linear-gradient(160deg,#5a6a40,#e9dcc5 45%,#b3323f)}
.img-flowers{background:linear-gradient(140deg,#f2e9d6,#e8b93a 40%,#c84a2a 65%,#7f9a55)}

/* footer */
.site-footer{position:absolute;top:3933px;left:0;width:1200px;height:407px;background:var(--white)}
.site-footer .brand{left:80px;top:90px}
.locations{position:absolute;left:64px;top:190px;display:flex}
.location{font-size:13px;line-height:24px}
.location h4{font-size:24px;line-height:32px;color:var(--gold);font-weight:400;margin-bottom:6px;white-space:nowrap;padding-right:4px}
.bottom-bar{position:absolute;top:4340px;left:0;width:1200px;height:52px;background:var(--dark);color:#eee;font-size:13px;padding:0 64px;display:flex;align-items:center;justify-content:space-between}
.bottom-bar .links{display:flex;gap:28px}
</style>
</head>
<body>

<header class="site-header">
  <div class="brand">HELGA WENDRICH</div>
  <div class="contact-top">
    <span><svg width="18" height="18" viewBox="0 0 24 24" fill="none" stroke="#e0067a" stroke-width="2"><path d="M22 16.9v3a2 2 0 0 1-2.2 2A19.8 19.8 0 0 1 2.1 4.2 2 2 0 0 1 4.1 2h3a2 2 0 0 1 2 1.7c.1 1 .4 1.9.7 2.8a2 2 0 0 1-.5 2.1L8 9.9a16 16 0 0 0 6 6l1.3-1.3a2 2 0 0 1 2.1-.4c.9.3 1.8.6 2.8.7a2 2 0 0 1 1.8 2z"/></svg>037100 / 4810</span>
    <span><svg width="20" height="20" viewBox="0 0 24 24" fill="none" stroke="#e0067a" stroke-width="2"><rect x="3" y="3" width="18" height="18" rx="2"/><rect x="7" y="6" width="10" height="4"/><path d="M7 14h2M11 14h2M15 14h2M7 17h2M11 17h2M15 17h2"/></svg>037100 / 4811</span>
  </div>
  <nav class="nav">
    <span class="active">Home</span><span>Services</span><span>Downloads</span><span>Gallery</span><span>Pursue</span><span>Locations</span><span>Contact</span>
  </nav>
</header>

<section class="hero">
  <div class="hero-photo" role="img" aria-label="White lilies with green leaves and a black mourning ribbon"></div>
  <div class="hero-card">
    <div class="band serif">Welcome to</div>
    <div class="t1 serif">Bestattung</div>
    <div class="t2 serif">Helga<br>Wendrich</div>
  </div>
  <svg class="call-btn" width="48" height="48" viewBox="0 0 48 48" aria-label="Call">
    <circle cx="24" cy="24" r="24" fill="#e0067a"/>
    <path d="M17 13c1 0 2 2 3 4s0 3-1 4c1 3 4 6 7 7 1-1 2-2 4-1s4 2 4 3-2 5-5 4c-8-2-14-8-16-16-1-3 3-5 4-5z" fill="#fff"/>
  </svg>
</section>

<section class="intro">
  <div class="kicker">Your competent and friendly contact person for over 30 years</div>
  <h2 class="serif">We are here<br>for you</h2>
  <span class="btn">We are here for you</span>
  <div class="copy">
    <p>We are happy to advise you on all decisions that need to be made in the event of a death and support you with handling many formalities. We will inform you about the types of burials, the possibility of a funeral home visit combined with a home visit, and the planning of funeral services in a religious or secular setting.</p>
    <p>We can take many tasks off your hands and relieve you of as much burden as possible!</p>
  </div>
</section>

<section class="services-head">
  <div class="kicker">We take the burden off your shoulders</div>
  <h2 class="serif">Services</h2>
  <span class="btn">Services</span>
</section>

<article class="service s1">
  <div class="photo" role="img" aria-label="Mourner in a dark suit holding a white rose"></div>
  <div class="text"><h3 class="serif">Planning</h3><p>When a death occurs in the family, relatives must plan the funeral within a few days. But what should bereaved relatives consider when organizing the funeral? We explain everything in detail.</p></div>
</article>
<article class="service s2">
  <div class="photo" role="img" aria-label="Pallbearers carrying a wooden coffin with white flowers across a lawn"></div>
  <div class="text"><h3 class="serif">Types of funerals</h3><p>You can choose between earth burials, cremations, and sea burials with ashes.</p></div>
</article>
<article class="service s3">
  <div class="photo" role="img" aria-label="Person in dark clothing holding white lilies"></div>
  <div class="text"><h3 class="serif">Care</h3><p>A loss often leaves a deep mark and always means change. "Where do I begin? What should I do with my life now, and what do I need to sort out?"</p></div>
</article>

<section class="impressions">
  <h2 class="serif">Impressions</h2>
  <div class="grid">
    <div class="cell img-coffin notch-up" role="img" aria-label="Light wooden coffin with a floral arrangement"></div>
    <div class="cell serif notch-down">Floral<br>arrangement</div>
    <div class="cell img-urn notch-up" role="img" aria-label="Cream urn surrounded by red roses"></div>
    <div class="cell serif">Coffins and coffin<br>arrangements</div>
    <div class="cell img-flowers" role="img" aria-label="Colourful bouquet of yellow, red and white flowers"></div>
    <div class="cell serif">Urns and urn<br>arrangements</div>
  </div>
</section>

<footer class="site-footer">
  <div class="brand">HELGA WENDRICH</div>
  <div class="locations">
    <div class="location" style="width:254px"><h4 class="serif">Birkwalde</h4>Lindenweg 7<br>09600 Birkwalde<br>037100 / 4810</div>
    <div class="location" style="width:213px"><h4 class="serif">Eichenstedt</h4>Am Markt 4<br>09610 Eichenstedt<br>037200 / 3390</div>
    <div class="location" style="width:232px"><h4 class="serif">Wiesenau</h4>Gartenstraße 18<br>09520 Wiesenau<br>03700 / 551204</div>
    <div class="location" style="width:215px"><h4 class="serif">Talbrück</h4>Mühlgasse 9<br>04730 Talbrück<br>034300 / 27815</div>
    <div class="location"><h4 class="serif">Lindholz</h4>Wiesenstraße 220<br>09140 Lindholz<br>0371 / 4409127</div>
  </div>
</footer>

<div class="bottom-bar">
  <span>© 2026 bestattung-helga-wendrich.de</span>
  <span class="links"><span>Imprint</span><span>Data protection</span></span>
</div>

</body>
</html>
```